CBD online business for pets and pet parents needs a new website

We need a website for my new online business. I have left a job of 25 years to do my passion. Helping Pets Live healthy and happy lives. I would like to provide my story so that our customer will know why I have started this business-To help!We will be providing all natural CBD (Hemp) products, specialty items, memorials as well as some products for pet parents. We would like our landing page to have our mission, be informative and easy to navigate and maybe feature our treats and oils for pets. We will need a page for pet products, a page for pet memorials, a page for pet lover products and a page for pet parent products.

Target Market(s)

millennials, boomers, pet lovers

Coding

Coded - Design and coding required

Number of Pages Required

5+ page

Colors
33b8a4

Requirements
Nice to have
• diagram of hemp oil extract benefits for dogs and people

```html
<!DOCTYPE html>
<html lang="en">
<head>
<meta charset="utf-8">
<title>Verdant Paws — Hemp Oil for Pets</title>
<link rel="stylesheet" href="https://fonts.googleapis.com/css2?family=Roboto:wght@400;500;700&display=swap">
<style>
:root{
  --green:#6ccb3a;
  --green-deep:#1f9a3d;
  --green-band:#1e9c3a;
  --green-mid:#7ed13f;
  --red:#d3262e;
  --ink:#222;
  --text:#444;
  --line:#e3e3e3;
  --footer:#2f2f2f;
  --white:#fff;
}
*{box-sizing:border-box;margin:0;padding:0}
html,body{width:1200px;height:4728px;overflow:hidden}
body{font-family:"Roboto",sans-serif;color:var(--text);background:var(--white);position:relative}
.abs{position:absolute}
.btn{position:absolute;display:flex;align-items:center;justify-content:center;border-radius:26px;font-size:13px;color:var(--white);background:var(--green-deep)}
.section-title{position:absolute;left:0;width:1200px;text-align:center;font-size:34px;font-weight:500;color:var(--ink)}

/* header */
.header{position:absolute;top:0;left:0;width:1200px;height:120px}
.menu{left:78px;top:55px;display:flex;align-items:center;gap:8px;font-size:13px;letter-spacing:1px;color:var(--ink)}
.brand{position:absolute;display:flex;align-items:center;gap:10px;font-family:"Roboto",sans-serif;font-weight:700;color:var(--green);white-space:nowrap}
.brand .dot{width:30px;height:30px;border-radius:50%;background:var(--green)}
.header .brand{left:505px;top:44px;font-size:30px}
.header-icons{right:78px;top:54px;display:flex;gap:22px}

/* hero */
.hero{position:absolute;top:120px;left:0;width:1200px;height:583px;background:linear-gradient(90deg,#4f5a3a 0%,#7d8a63 35%,#a39a83 60%,#7c9a55 100%)}
.hero h1{position:absolute;left:76px;top:228px;font-size:36px;font-weight:500;color:var(--white)}
.hero p{position:absolute;left:78px;top:278px;width:300px;font-size:13px;letter-spacing:1px;line-height:16px;color:var(--white)}
.hero .outline{position:absolute;left:80px;top:345px;width:187px;height:46px;border:2px solid var(--white);border-radius:26px;color:var(--white);font-size:13px;display:flex;align-items:center;justify-content:center}

/* features */
.feature{position:absolute;top:617px;width:260px;text-align:center}
.feature .ring{width:176px;height:176px;border-radius:50%;background:var(--green);border:6px solid var(--white);margin:0 auto;display:flex;align-items:center;justify-content:center}
.feature h3{margin-top:22px;font-size:19px;font-weight:400;letter-spacing:1.5px;line-height:24px;color:var(--ink)}

/* about */
.about h2{position:absolute;left:78px;top:948px;font-size:36px;font-weight:400;color:var(--ink)}
.about p{position:absolute;left:80px;width:500px;font-size:13px;letter-spacing:.6px;line-height:16px;color:var(--text)}
.about-photo{position:absolute;left:680px;top:960px;width:415px;height:330px;border-radius:6px;background:radial-gradient(ellipse at center,#b48a5a 0%,#8a6a4a 40%,#f4f1ec 72%)}
.play{position:absolute;left:860px;top:1145px;width:40px;height:40px;border-radius:50%;border:3px solid var(--white);background:rgba(0,0,0,.35)}

/* products */
.product{position:absolute;top:1432px;width:238px}
.product .frame{height:248px;border:1px solid var(--line);display:flex;align-items:center;justify-content:center}
.product .shot{width:110px;height:210px;border-radius:8px}
.product .name{margin-top:20px;text-align:center;font-size:14px;letter-spacing:1.5px;color:var(--text)}
.product .price{margin-top:6px;text-align:center;font-size:20px;letter-spacing:1.5px;color:var(--red)}

/* benefits */
.benefits{position:absolute;top:1900px;left:0;width:1200px;height:528px;background:linear-gradient(180deg,#f4f4f4 0%,#e6e6e6 100%)}
.benefits .shot{position:absolute;left:160px;top:60px;width:340px;height:435px;border-radius:6px;background:linear-gradient(135deg,#8fd152 0%,#f5f5f0 55%,#7a3e1a 100%)}
.benefits h2{position:absolute;left:598px;top:150px;font-size:34px;font-weight:400;color:var(--ink)}
.benefits .sub{position:absolute;left:600px;top:202px;font-size:19px;line-height:24px;color:var(--ink)}
.benefits .price{position:absolute;left:600px;top:252px;font-size:19px;color:var(--red)}
.benefits .note{position:absolute;left:600px;top:292px;width:520px;font-size:12px;line-height:16px;color:var(--ink)}

/* why */
.why{position:absolute;top:2428px;left:0;width:1200px;height:520px;background:var(--green-band)}
.why h2{position:absolute;left:0;width:1200px;top:52px;text-align:center;font-size:32px;font-weight:700;color:var(--white)}
.why-item{position:absolute;width:240px;text-align:center;color:var(--white)}
.why-item h4{font-size:19px;font-weight:400}
.why-item p{font-size:12px;line-height:16px;margin-top:3px}

/* blogs */
.blog{position:absolute;top:3073px;width:336px;height:367px;border:1px solid var(--line);padding:14px}
.blog .photo{width:308px;height:205px}
.blog .meta{margin-top:28px;font-size:13px;color:var(--ink)}
.blog h4{margin-top:12px;font-size:13px;font-weight:500;color:var(--ink)}
.blog p{margin-top:6px;font-size:13px;line-height:15px;color:var(--text)}
.blog .more{margin-top:18px;font-size:13px;color:var(--text)}

/* testimonials */
.testi{position:absolute;top:3637px;width:315px;height:283px;border:1px solid #d8d8d8;text-align:center}
.testi .quote{position:absolute;left:18px;top:-22px;width:44px;height:44px;border-radius:50%;background:var(--green-deep);color:var(--white);font-size:28px;font-weight:700;line-height:50px}
.testi .avatar{width:92px;height:92px;border-radius:50%;margin:28px auto 0}
.testi h4{margin-top:12px;font-size:18px;font-weight:500;color:var(--ink)}
.testi .role{font-size:14px;color:var(--green)}
.testi p{margin:10px auto 0;width:230px;font-size:13px;line-height:16px;color:var(--text)}
.testi .stars{margin-top:8px;color:#f0a82a;font-size:12px;letter-spacing:3px}

/* promos */
.promo{position:absolute;top:4150px;width:327px;height:158px;display:flex;align-items:center;gap:18px;padding-left:28px;color:var(--white)}
.promo h4{font-size:18px;font-weight:500}
.promo p{font-size:14px;line-height:17px}

/* footer */
.footer{position:absolute;top:4360px;left:0;width:1200px;height:368px;background:var(--footer);color:#ddd}
.footer h5{position:absolute;top:62px;font-size:15px;font-weight:500;color:var(--white)}
.footer ul{position:absolute;top:104px;list-style:none;font-size:13px;line-height:24px}
.footer ul li::before{content:"›";margin-right:12px}
.contact{position:absolute;left:80px;top:130px;font-size:14px;line-height:24px}
.contact .row{display:flex;gap:10px;align-items:flex-start}
.contact svg{margin-top:6px;flex:none}
.social li::before{content:none!important}
.social span{display:inline-block;width:17px;height:17px;border-radius:50%;margin-right:14px;vertical-align:-3px}
.copy{position:absolute;left:0;top:300px;width:1200px;height:68px;background:var(--white);color:var(--ink);font-size:13px;padding:20px 80px}
.pay{position:absolute;top:16px;display:flex;gap:6px;right:80px}
.pay div{width:48px;height:30px;border:1px solid #ccc;border-radius:3px;font-size:10px;font-weight:700;display:flex;align-items:center;justify-content:center;color:#555}
</style>
</head>
<body>

<header class="header">
  <div class="abs menu">
    <svg width="20" height="14"><rect y="1" width="20" height="2" fill="#222"/><rect y="6" width="20" height="2" fill="#222"/><rect y="11" width="14" height="2" fill="#222"/></svg>MENU
  </div>
  <div class="brand"><span class="dot"></span>Verdant Paws</div>
  <div class="abs header-icons">
    <svg width="16" height="16" fill="none" stroke="#222" stroke-width="1.6"><circle cx="6.5" cy="6.5" r="5"/><path d="M10.5 10.5l4 4"/></svg>
    <svg width="16" height="16" fill="none" stroke="#222" stroke-width="1.6"><circle cx="8" cy="5" r="3.5"/><path d="M2 15c1-4 11-4 12 0"/></svg>
    <svg width="18" height="16" fill="none" stroke="#222" stroke-width="1.6"><path d="M9 15s-7-4.5-7-9a3.6 3.6 0 017-1.2A3.6 3.6 0 0116 6c0 4.5-7 9-7 9z"/></svg>
    <svg width="18" height="16" fill="none" stroke="#222" stroke-width="1.6"><path d="M1 2h3l2 9h9l2-6H5"/><circle cx="7" cy="14" r="1.3"/><circle cx="14" cy="14" r="1.3"/></svg>
  </div>
</header>

<section class="hero" role="img" aria-label="Photo of a smiling woman hugging a small dog outdoors">
  <h1>Hemp Oil For Pets</h1>
  <p>Delicious, Mouth-watering CBD Oils &amp; Treats</p>
  <div class="outline">Read More</div>
</section>

<div class="feature" style="left:130px">
  <div class="ring"><svg width="80" height="80" fill="none" stroke="#fff" stroke-width="4"><circle cx="40" cy="34" r="22"/><path d="M30 34l7 7 14-14M28 52l-6 22 12-6 6 10 4-20M52 52l6 22-12-6"/></svg></div>
  <h3>Certified USDA<br>Organic Hemp Farm</h3>
</div>
<div class="feature" style="left:467px">
  <div class="ring"><svg width="80" height="80" fill="#fff"><path d="M40 10c10 8 10 24 0 30-10-6-10-22 0-30zM20 24c10 0 18 8 18 18-10 0-18-8-18-18zM60 24c-10 0-18 8-18 18 10 0 18-8 18-18z"/><path d="M10 56h18l14 6 18-10c4 0 5 4 2 6L42 70H10z"/></svg></div>
  <h3>Natural &amp; Organic<br>Ingredients</h3>
</div>
<div class="feature" style="left:838px">
  <div class="ring"><svg width="80" height="80" fill="#fff"><path d="M40 8c6 12 6 28 0 40-6-12-6-28 0-40zM14 26c14 2 22 12 26 22-12 0-22-8-26-22zM66 26c-14 2-22 12-26 22 12 0 22-8 26-22zM12 50c10-4 20-2 28 0-8 6-18 6-28 0zM68 50c-10-4-20-2-28 0 8 6 18 6 28 0z"/><rect x="38.5" y="48" width="3" height="20"/></svg></div>
  <h3>Full Spectrum<br>Cannabinoids</h3>
</div>

<section class="about">
  <h2>About us</h2>
  <p style="top:1016px">Lorem Ipsum is simply dummy text of the printing and typesetting industry. Lorem Ipsum has been the industry's standard dummy text ever since the 1500s,</p>
  <p style="top:1082px">when an unknown printer took a galley of type and scrambled it to make a type specimen book. It has survived not only five centuries, but also the leap into electronic typesetting, remaining essentially unchanged.</p>
  <div class="btn" style="left:78px;top:1182px;width:188px;height:48px">Read More</div>
  <div class="about-photo" role="img" aria-label="Photo of a group of five dogs of different breeds sitting together"></div>
  <div class="play"></div>
</section>

<h2 class="section-title" style="top:1342px">Featured Products</h2>
<div class="product" style="left:80px"><div class="frame"><div class="shot" role="img" aria-label="Hemp seed oil bottle for pets" style="background:linear-gradient(180deg,#2d6b5a,#d9c9a2 50%,#3f7a6a)"></div></div><div class="name">Product Name</div><div class="price">$00.00</div></div>
<div class="product" style="left:348px"><div class="frame"><div class="shot" role="img" aria-label="Amber dropper bottle of hemp oil" style="background:linear-gradient(180deg,#1a1a1a 20%,#8a4a1e 45%,#e8f0e0 70%,#6a3a16)"></div></div><div class="name">Product Name</div><div class="price">$00.00</div></div>
<div class="product" style="left:617px"><div class="frame"><div class="shot" role="img" aria-label="Blue dropper bottle of CBD oil" style="background:linear-gradient(180deg,#e4eef6 20%,#1d4f8a 45%,#e86a1a 75%,#1d4f8a)"></div></div><div class="name">Product Name</div><div class="price">$00.00</div></div>
<div class="product" style="left:885px"><div class="frame"><div class="shot" role="img" aria-label="Dark dropper bottle of pet CBD oil" style="background:linear-gradient(180deg,#1a1a1a 20%,#6a2a1a 45%,#c63a2a 70%,#3a1a12)"></div></div><div class="name">Product Name</div><div class="price">$00.00</div></div>
<div class="btn" style="left:513px;top:1798px;width:187px;height:48px">Vieww More</div>

<section class="benefits">
  <div class="shot" role="img" aria-label="Hemp oil bottle standing beside its green retail box"></div>
  <h2>Benefits</h2>
  <div class="sub">The Kind Leaf Full Spectrum<br>Hemp Oil for Dogs</div>
  <div class="price">$00.00</div>
  <div class="note">300mg / 30ml - Natural Organic Dog Calming Aid - Separation Anxiety Relief/ Relieve Pain &amp; Joint Inflammation in Canine Arthritis - Treats Seizures</div>
  <div class="btn" style="left:600px;top:353px;width:188px;height:46px">Add To Cart</div>
</section>

<section class="why">
  <h2>Why CBD Use ?</h2>
  <svg class="abs" style="left:0;top:0" width="1200" height="520" fill="none" stroke="var(--green-mid)" stroke-width="3">
    <path d="M321 170h140M240 275h195M320 367h150M880 170H748M960 276H766M880 374H730"/>
    <circle cx="600" cy="262" r="160" fill="var(--green-mid)" stroke="none"/>
    <circle cx="600" cy="262" r="110" fill="none" stroke="#95dc5c" stroke-width="2"/>
    <g fill="var(--green-mid)" stroke="var(--white)" stroke-width="3">
      <circle cx="482" cy="170" r="14"/><circle cx="436" cy="275" r="14"/><circle cx="469" cy="367" r="14"/>
      <circle cx="720" cy="170" r="14"/><circle cx="760" cy="276" r="14"/><circle cx="728" cy="374" r="14"/>
    </g>
  </svg>
  <div class="why-item" style="left:202px;top:180px"><h4>Anticonvusant</h4><p>Lorem Ipsum is simply dummy text<br>and typesetting industry.</p></div>
  <div class="why-item" style="left:122px;top:284px"><h4>Anticonvusant</h4><p>Lorem Ipsum is simply dummy text<br>and typesetting industry.</p></div>
  <div class="why-item" style="left:200px;top:378px"><h4>Anticonvusant</h4><p>Lorem Ipsum is simply dummy text<br>and typesetting industry.</p></div>
  <div class="why-item" style="left:774px;top:184px"><h4>Anticonvusant</h4><p>Lorem Ipsum is simply dummy text<br>and typesetting industry.</p></div>
  <div class="why-item" style="left:838px;top:284px"><h4>Anticonvusant</h4><p>Lorem Ipsum is simply dummy text<br>and typesetting industry.</p></div>
  <div class="why-item" style="left:754px;top:390px"><h4>Anticonvusant</h4><p>Lorem Ipsum is simply dummy text<br>and typesetting industry.</p></div>
</section>

<h2 class="section-title" style="top:3002px">Blogs</h2>
<article class="blog" style="left:64px"><div class="photo" role="img" aria-label="Photo of a small terrier walking on grass" style="background:linear-gradient(135deg,#8a8f7a,#a7865a 55%,#6f7a4a)"></div><div class="meta">By Admin &nbsp;&nbsp;| &nbsp;&nbsp;22 June, 2019</div><h4>What is Lorem Ipsum?</h4><p>Lorem Ipsum is simply dummy &nbsp;the printing a typesetting industry.</p><div class="more">Continue..◎</div></article>
<article class="blog" style="left:432px"><div class="photo" role="img" aria-label="Photo of a person cuddling a white puppy" style="background:linear-gradient(135deg,#3a4a52,#9aa6ae 50%,#e8ecee)"></div><div class="meta">By Admin &nbsp;&nbsp;| &nbsp;&nbsp;22 June, 2019</div><h4>What is Lorem Ipsum?</h4><p>Lorem Ipsum is simply dummy &nbsp;the printing a typesetting industry.</p><div class="more">Continue..◎</div></article>
<article class="blog" style="left:798px"><div class="photo" role="img" aria-label="Photo of a woman smiling with a beagle puppy" style="background:linear-gradient(135deg,#5a3a2a,#c89a6a 50%,#8a8a3a)"></div><div class="meta">By Admin &nbsp;&nbsp;| &nbsp;&nbsp;22 June, 2019</div><h4>What is Lorem Ipsum?</h4><p>Lorem Ipsum is simply dummy &nbsp;the printing a typesetting industry.</p><div class="more">Continue..◎</div></article>
<div class="btn" style="left:508px;top:3472px;width:188px;height:48px">View More</div>

<h2 class="section-title" style="top:3555px">Testimonials</h2>
<div class="testi" style="left:80px"><div class="quote">“</div><div class="avatar" role="img" aria-label="Customer portrait" style="background:#c9a88a"></div><h4>Daniel Hart</h4><div class="role">Creative Director</div><p>Lorem Ipsum simply dummy text in printingand types &nbsp;industry simply psum is simply dummy</p><div class="stars">★★★★★</div></div>
<div class="testi" style="left:444px"><div class="quote">“</div><div class="avatar" role="img" aria-label="Customer portrait" style="background:#b08a6a"></div><h4>Maya Lane</h4><div class="role">Creative Director</div><p>Lorem Ipsum simply dummy text in printingand types &nbsp;industry simply psum is simply dummy</p><div class="stars">★★★★★</div></div>
<div class="testi" style="left:805px"><div class="quote">“</div><div class="avatar" role="img" aria-label="Customer portrait" style="background:#8a5a3a"></div><h4>Nora Wells</h4><div class="role">Creative Director</div><p>Lorem Ipsum simply dummy text in printingand types &nbsp;industry simply psum is simply dummy</p><div class="stars">★★★★★</div></div>
<svg class="abs" style="left:582px;top:3944px" width="36" height="10"><circle cx="5" cy="5" r="3.5" fill="var(--green-deep)"/><circle cx="18" cy="5" r="3.5" fill="#888"/><circle cx="31" cy="5" r="3.5" fill="#888"/></svg>

<h2 class="section-title" style="top:3988px;font-size:32px">Join Our Newletter</h2>
<div class="abs" style="left:0;width:1200px;top:4032px;text-align:center;font-size:13px">Lorem Ipsum is simply dummy.</div>
<div class="abs" style="left:316px;top:4066px;width:420px;height:40px;border:1px solid var(--line);border-radius:20px;padding:12px 22px;font-size:13px;font-style:italic;color:#999">Email Here</div>
<div class="btn" style="left:746px;top:4066px;width:158px;height:40px">Submit</div>

<div class="promo" style="left:80px;background:var(--green)"><svg width="44" height="32" fill="none" stroke="#fff" stroke-width="2"><path d="M2 4h24v20H2zM26 12h9l6 7v5H26"/><circle cx="10" cy="26" r="3.5"/><circle cx="34" cy="26" r="3.5"/></svg><div><h4>Free Shipping Worldwide</h4><p>On Order<br>Over 15 Days a week</p></div></div>
<div class="promo" style="left:437px;background:var(--green-deep)"><svg width="40" height="36" fill="none" stroke="#fff" stroke-width="2"><path d="M6 20v-4a14 14 0 0128 0v4"/><rect x="3" y="20" width="7" height="11" rx="2"/><rect x="30" y="20" width="7" height="11" rx="2"/><path d="M34 31c0 3-4 4-10 4"/></svg><div><h4>24/7 Customer Service</h4><p>Call us 24/7<br>000 111 222 333</p></div></div>
<div class="promo" style="left:793px;background:var(--green)"><svg width="40" height="30" fill="none" stroke="#fff" stroke-width="2"><path d="M4 12l16-9 16 9-16 15z"/><circle cx="20" cy="12" r="3"/></svg><div><h4>Save 15%</h4><p>with the Verdant Paws</p></div></div>

<footer class="footer">
  <div class="brand" style="left:80px;top:68px;font-size:32px"><span class="dot" style="width:40px;height:40px"></span>Verdant Paws</div>
  <div class="contact">
    <div class="row"><svg width="10" height="13" fill="#ddd"><path d="M5 0a5 5 0 015 5c0 3.5-5 8-5 8S0 8.5 0 5a5 5 0 015-5z"/><circle cx="5" cy="5" r="1.8" fill="#2f2f2f"/></svg><div>48 Orchard Lane<br>Millbrook, USA</div></div>
    <div class="row"><svg width="10" height="12" fill="#ddd"><path d="M2 0l3 3-1.5 2a8 8 0 003.5 3.5L9 7l1 3-2 2C3 11 0 6 0 2z"/></svg><div>(00)-555-010-2040</div></div>
    <div class="row"><svg width="12" height="9" fill="none" stroke="#ddd" stroke-width="1.4"><rect x=".7" y=".7" width="10.6" height="7.6"/><path d="M1 1l5 4 5-4"/></svg><div>sales@verdantpaws.com</div></div>
  </div>
  <h5 style="left:475px">Quick Link</h5>
  <ul style="left:475px"><li>My Account</li><li>Cart Page</li><li>Personal info</li><li>wishlist</li><li>Gifts</li><li>Terms and Conditions</li></ul>
  <h5 style="left:738px">Quick link</h5>
  <ul style="left:738px"><li>Home</li><li>About us</li><li>Products</li><li>Testimonials</li><li>Blog</li><li>Contact us</li></ul>
  <h5 style="left:1020px">Follow us</h5>
  <ul class="social" style="left:1020px;top:100px">
    <li><span style="background:#3b5998"></span>Friendbook</li>
    <li><span style="background:#d6266f"></span>Snapgram</li>
    <li><span style="background:#1da1f2"></span>Chirper</li>
    <li><span style="background:#0a66c2"></span>Workline</li>
  </ul>
  <div class="copy">Copyright © 2019 Verdant Paws. All Rights Reserved.
    <div class="pay"><div>Orbit</div><div>Nova</div><div>Pulse</div><div>Crest</div><div>Shopa</div></div>
  </div>
</footer>

</body>
</html>
```